Pheasant Farm needs a logo design

I need a logo design for my Pheasant farm. We raise Pheasants from chicks to adult birds for the hunting clubs dog training and restocking. I would like a logo that makes it easy to see that we deal with Pheasants. My company name is Larkin Meadow Pines located in northern MN. I'd like a pheasant in the logo if possible.

Target Market(s)

Hunting clubs, dog trainers, hunters

Contact Information for Business Card

Larkin Meadow Pines Dale Wexby cell 715-463-2098 office 218-302-7746 tallgrassfowlyard.com tallgrassfowlyard@quailpostmail.com
5816 Bramwell Rd NE
Fernholt, Birchland 56519

```html
<!DOCTYPE html>
<html lang="en">
<head>
<meta charset="utf-8">
<title>Larkin Meadow Pines – Business Card</title>
<link rel="stylesheet" href="https://fonts.googleapis.com/css2?family=Open+Sans:ital,wght@0,400;0,600;0,700;1,400&display=swap">
<style>
  :root {
    --page: #e4e2de;
    --cream-light: #f1e9da;
    --cream: #e6dac4;
    --brown: #5b4526;
    --brown-dark: #46341b;
    --band-text: #f3ebdc;
    --wood-light: #e9cfa9;
    --wood-mid: #d8b283;
    --wood-dark: #c99a6b;
  }
  * { box-sizing: border-box; margin: 0; padding: 0; }
  html, body { width: 1200px; height: 900px; overflow: hidden; }
  body {
    background: var(--page);
    font-family: "Open Sans", Arial, sans-serif;
    display: flex;
    flex-direction: column;
    align-items: center;
    justify-content: center;
    gap: 40px;
  }
  .card {
    position: relative;
    width: 665px;
    height: 380px;
    overflow: hidden;
    box-shadow: 0 10px 28px rgba(0,0,0,0.22);
  }

  /* Back side */
  .card-back .wood {
    position: absolute; inset: 0;
    background: linear-gradient(100deg, var(--wood-light) 0%, var(--wood-mid) 45%, var(--wood-light) 70%, var(--wood-dark) 100%);
  }
  .card-back .brand {
    position: absolute; inset: 0;
    display: flex; align-items: center; justify-content: center;
  }

  .brand-name {
    font-weight: 700;
    color: var(--brown);
    letter-spacing: 1px;
    text-transform: uppercase;
    text-align: center;
    line-height: 1.15;
  }
  .card-back .brand-name { font-size: 40px; }

  /* Front side */
  .card-front {
    background: linear-gradient(160deg, var(--cream-light) 0%, var(--cream) 100%);
  }
  .card-front .brand {
    position: absolute;
    left: 360px; top: 60px;
    width: 260px;
    display: flex; justify-content: center;
  }
  .card-front .brand-name { font-size: 30px; }

  .person {
    position: absolute;
    left: 52px; top: 150px;
    color: var(--brown);
  }
  .person-name { font-size: 18px; font-weight: 700; }
  .person-role { font-size: 13px; font-style: italic; margin-top: -2px; }

  .band {
    position: absolute;
    left: 0; right: 0;
    top: 218px; height: 128px;
    background: linear-gradient(90deg, var(--brown-dark), var(--brown));
  }
  .contacts {
    position: absolute;
    left: 46px; top: 228px;
    list-style: none;
    color: var(--band-text);
    font-size: 15.5px;
  }
  .contacts li {
    display: flex; align-items: center; gap: 9px;
    height: 26px;
  }
  .contacts svg, .address svg { flex: none; }
  .address {
    position: absolute;
    left: 400px; top: 250px;
    display: flex; gap: 8px;
    color: var(--band-text);
    font-size: 16.5px;
    line-height: 1.4;
  }
</style>
</head>
<body>

  <section class="card card-back">
    <div class="wood" role="img" aria-label="Light natural wood grain texture"></div>
    <div class="brand">
      <p class="brand-name">Larkin Meadow Pines</p>
    </div>
  </section>

  <section class="card card-front">
    <div class="brand">
      <p class="brand-name">Larkin<br>Meadow Pines</p>
    </div>

    <div class="person">
      <p class="person-name">Dale Wexby</p>
      <p class="person-role">Owner</p>
    </div>

    <div class="band"></div>

    <ul class="contacts">
      <li>
        <svg width="14" height="14" viewBox="0 0 24 24" fill="currentColor" aria-hidden="true"><path d="M6.6 10.8a15.1 15.1 0 0 0 6.6 6.6l2.2-2.2a1 1 0 0 1 1-.25 11.4 11.4 0 0 0 3.6.57 1 1 0 0 1 1 1V20a1 1 0 0 1-1 1A17 17 0 0 1 3 4a1 1 0 0 1 1-1h3.5a1 1 0 0 1 1 1c0 1.25.2 2.45.57 3.57a1 1 0 0 1-.25 1z"/></svg>
        <span>218-302-7746</span>
      </li>
      <li>
        <svg width="14" height="16" viewBox="0 0 14 22" fill="none" stroke="currentColor" stroke-width="1.6" aria-hidden="true"><rect x="1" y="1" width="12" height="20" rx="2"/><line x1="5" y1="18" x2="9" y2="18"/></svg>
        <span>715-463-2098</span>
      </li>
      <li>
        <svg width="16" height="12" viewBox="0 0 20 14" fill="none" stroke="currentColor" stroke-width="1.5" aria-hidden="true"><rect x="1" y="1" width="18" height="12"/><polyline points="1,1 10,8 19,1"/></svg>
        <span>tallgrassfowlyard@quailpostmail.com</span>
      </li>
      <li>
        <svg width="16" height="16" viewBox="0 0 20 20" fill="none" stroke="currentColor" stroke-width="1.3" aria-hidden="true"><circle cx="10" cy="10" r="8.5"/><ellipse cx="10" cy="10" rx="3.8" ry="8.5"/><line x1="1.5" y1="10" x2="18.5" y2="10"/><line x1="3" y1="5.5" x2="17" y2="5.5"/><line x1="3" y1="14.5" x2="17" y2="14.5"/></svg>
        <span>tallgrassfowlyard.com</span>
      </li>
    </ul>

    <div class="address">
      <svg width="16" height="22" viewBox="0 0 16 22" fill="none" stroke="currentColor" stroke-width="1.8" aria-hidden="true"><path d="M8 21s-7-7.2-7-12a7 7 0 0 1 14 0c0 4.8-7 12-7 12z"/><circle cx="8" cy="9" r="2.6"/></svg>
      <p>5816 Bramwell Rd NE<br>Fernholt, Birchland 56519</p>
    </div>
  </section>

</body>
</html>
```